Blue Ridge Haulers Website (quoting web application)

We need a website designed for our furniture moving company in Cape Town, South Africa.

I have attached some logos and images for you to use.

I have also attached the layout of the three pages we want designed (pdf file)

Dark blue is our colour.

The pictures of our trucks (uploaded) epitomise the design required.

Our old site (existing) is viewable here: blueridgehaulers.co.za

Target Market(s)

People moving house in Cape Town, South Africa.

Number of Pages Required

3 page

Font styles to use
Sans Serif

Colors
0255a3

Requirements
Must have
• Page design for the 3 pages in the pdf file.

```html
<!DOCTYPE html>
<html lang="en">
<head>
<meta charset="utf-8">
<title>Blue Ridge Haulers – Website Pages</title>
<link href="https://fonts.googleapis.com/css2?family=Roboto:wght@400;500;700&display=swap" rel="stylesheet">
<style>
:root{
  --canvas:#acacac;
  --navy:#0b1d93;
  --navy-deep:#081570;
  --blue:#2547c9;
  --tab-active:#1d48d6;
  --white:#ffffff;
  --ink:#333333;
  --muted:#666666;
  --line:#d6d6d6;
  --footer:#1d1d1d;
  --green:#2bb34a;
  --grey-btn:#b7b7b7;
}
*{box-sizing:border-box;margin:0;padding:0}
html,body{width:1200px;height:1149px;overflow:hidden}
body{background:var(--canvas);font-family:'Roboto',sans-serif;color:var(--ink);position:relative}
.page{position:absolute;background:var(--white);overflow:hidden}
.abs{position:absolute}

/* brand */
.brand{display:flex;align-items:center;gap:5px;color:var(--white);font-weight:700;font-size:9px;letter-spacing:.3px;white-space:nowrap}
.brand-mark{width:12px;height:12px;border:1.5px solid var(--white)}

/* home page */
.home{left:44px;top:51px;width:529px;height:622px}
.hero{left:0;top:0;width:529px;height:262px;background:linear-gradient(160deg,#3a5fb8 0%,#23418f 45%,#152a6e 100%)}
.hero-brand{left:80px;top:11px}
.user-mail{left:300px;top:16px;color:var(--white);font-size:7px;display:flex;align-items:center;gap:4px}
.btn-logout{width:46px;height:19px;border-radius:10px;background:var(--navy);color:var(--white);font-size:6px;display:flex;align-items:center;justify-content:center;letter-spacing:.3px}
.hero-title{left:0;width:529px;top:69px;text-align:center;color:var(--white);font-weight:700;font-size:17px;letter-spacing:.5px}
.hero-tag{left:0;width:529px;top:102px;text-align:center;color:var(--white);font-size:7px}
.btn-quote{left:218px;top:122px;width:96px;height:22px;border:1.5px solid var(--white);border-radius:12px;color:var(--white);font-size:9px;display:flex;align-items:center;justify-content:center}
.chat{left:365px;top:139px;width:110px;height:123px;background:var(--white)}
.chat-head{height:15px;background:var(--tab-active);color:var(--white);font-size:6.5px;padding:4px 9px}
.chat-body{padding:6px 9px;font-size:4.2px;color:var(--muted);line-height:1.6}
.chat-field{border-bottom:1px solid var(--line);padding-top:5px;height:15px;font-size:4.2px;color:var(--ink)}
.chat-btn{margin-top:7px;height:14px;background:var(--navy);color:var(--white);font-size:4.8px;display:flex;align-items:center;justify-content:center}
.sec-title{color:var(--navy);font-weight:700;font-size:13px;text-align:center;left:0;width:529px}
.small-center{left:0;width:529px;text-align:center;font-size:6.5px;color:var(--ink)}
.review{top:339px;width:86px;height:30px;border:1px solid var(--line);display:flex;align-items:center;justify-content:center;font-size:12px;font-weight:700;color:var(--navy)}
.divider{left:0;top:403px;width:529px;height:1px;background:#ececec}
.service{top:443px;width:69px;height:59px;border:1px solid var(--line);display:flex;flex-direction:column;align-items:center;justify-content:flex-end;padding-bottom:9px;font-size:7px;color:var(--navy);gap:6px}
.service-icon{width:22px;height:22px;border:1.5px solid var(--navy);border-radius:2px}
.perks{left:0;top:516px;width:529px;text-align:center;font-size:6px;font-weight:700;color:var(--ink)}

/* footer */
.footer{left:0;width:100%;height:84px;background:var(--footer);color:#bdbdbd;font-size:4.6px}
.f-contact{line-height:2.6}
.f-btn{display:inline-block;background:var(--white);color:var(--ink);padding:2px 5px;font-size:4.6px;margin-top:2px}
.f-social{display:flex;gap:3px}
.f-social span{width:9px;height:9px;border:1px solid #cfcfcf;border-radius:50%}
.f-links{line-height:2}
.f-rule{height:1px;background:#444}
.f-copy{width:100%;text-align:center;left:0}

/* quote page */
.quote{left:614px;top:51px;width:528px;height:1014px}
.q-header{left:0;top:0;width:528px;height:46px;background:var(--navy)}
.nav{top:22px;display:flex;gap:0;font-size:6.3px;color:var(--white);letter-spacing:.2px}
.tabs{left:0;top:46px;width:528px;height:26px;background:linear-gradient(180deg,#1638b4,#0d2598);display:flex}
.tab{height:26px;display:flex;align-items:center;justify-content:center;color:var(--white);font-size:7px;border-right:1px solid rgba(255,255,255,.25)}
.tab.active{background:var(--tab-active)}
.vehicle-sec{left:0;top:72px;width:528px;height:195px;background:var(--navy)}
.q-heading{font-size:14px;color:var(--white)}
.vehicle{top:121px;height:112px;background:var(--white);border:1px solid #c9c9c9;display:flex;flex-direction:column;align-items:center;padding-top:12px}
.vehicle-art{width:62px;height:58px;background:linear-gradient(150deg,#4b63b8,#1f2f7a);border-radius:4px}
.vehicle-label{margin-top:10px;font-size:6.3px;display:flex;align-items:center;gap:4px;color:var(--ink)}
.check{width:9px;height:9px;border:1px solid #999;background:var(--white);display:inline-flex;align-items:center;justify-content:center}
.vehicle-note{font-size:3.8px;color:var(--ink);margin-top:3px}
.date-sec{left:0;top:267px;width:528px;height:304px;background:linear-gradient(100deg,#c8c8c8,#e3e3e3 50%,#cfd9e0)}
.date-heading{left:80px;top:285px;font-size:14px;color:var(--navy)}
.cal{left:123px;top:314px;width:285px;height:224px;background:var(--white);border:1px solid #bbb}
.cal-head{height:21px;background:var(--navy);color:var(--white);display:flex;align-items:center;justify-content:space-between;padding:0 8px;font-size:9px}
.cal-grid{display:grid;grid-template-columns:repeat(7,1fr)}
.dow{height:24px;display:flex;align-items:center;justify-content:center;font-size:9px;color:var(--navy)}
.day{height:36px;border-top:1px solid #c8c8c8;border-right:1px solid #c8c8c8;display:flex;flex-direction:column;align-items:center;justify-content:center;font-size:9px;color:#111;line-height:1.15}
.day:nth-child(7n){border-right:none}
.day small{font-size:6.5px}
.day.sel{background:var(--navy);color:var(--white)}
.price-heading{left:80px;top:597px;font-size:14px;color:var(--navy)}
.price-box{left:120px;top:627px;width:288px;height:203px;border:1px solid #d8d8d8;background:var(--white);font-size:6.8px;color:var(--muted)}
.row{position:absolute;left:19px}
.row .val{position:absolute;left:116px;top:0;white-space:nowrap}
.row.total{color:var(--navy);font-weight:700}
.row.total .note{position:absolute;left:172px;top:0;font-weight:400;color:var(--muted)}
.row.plain{color:var(--ink);font-size:6.3px}
.tick-box{display:inline-block;width:13px;height:9px;background:#e4e4e4;border:1px solid #ccc;vertical-align:middle;margin-left:6px}
.radio{left:122px;font-size:5.6px;color:var(--navy);display:flex;align-items:center;gap:4px}
.radio i{width:9px;height:9px;border:1px solid #999;border-radius:50%;display:inline-flex;align-items:center;justify-content:center}
.radio i b{width:5px;height:5px;border-radius:50%;background:#999}
.btn{display:flex;align-items:center;justify-content:center;color:var(--white);font-size:6px}
</style>
</head>
<body>

<!-- HOME PAGE -->
<section class="page home">
  <div class="abs hero" role="img" aria-label="Photo of the moving crew in blue overalls standing in front of a branded removal truck"></div>
  <div class="abs brand hero-brand"><span class="brand-mark"></span>BLUE RIDGE HAULERS</div>
  <div class="abs user-mail">
    <svg width="8" height="6" viewBox="0 0 8 6"><rect x=".5" y=".5" width="7" height="5" fill="none" stroke="#fff"/><path d="M.5 .5 4 3.3 7.5 .5" fill="none" stroke="#fff"/></svg>
    jo.naidoo@mailbox.co.za
  </div>
  <div class="abs btn-logout" style="left:401px;top:10px">LOGOUT</div>
  <div class="abs hero-title">BLUE RIDGE HAULERS</div>
  <div class="abs hero-tag">Trusted Cape Town Moves</div>
  <div class="abs btn-quote">Instant Quote</div>
  <div class="abs chat">
    <div class="chat-head">Can We Help?</div>
    <div class="chat-body">
      Please enter your name and email address to begin chatting with us
      <div class="chat-field">Name</div>
      <div class="chat-field">Email address</div>
      <div class="chat-field" style="height:20px">Message</div>
      <div class="chat-btn">INITIATE CHAT</div>
    </div>
  </div>

  <h2 class="abs sec-title" style="top:297px">Why choose us?</h2>
  <p class="abs small-center" style="top:320px">See what our customers say :</p>
  <div class="abs review" style="left:130px">FriendWall</div>
  <div class="abs review" style="left:222px">SearchPro</div>
  <div class="abs review" style="left:315px">RateLocal</div>
  <div class="abs divider"></div>

  <p class="abs small-center" style="top:423px;font-size:7px">We do all the special services :</p>
  <div class="abs service" style="left:92px"><span class="service-icon" role="img" aria-label="Hoisting icon"></span>Hoisting</div>
  <div class="abs service" style="left:158px"><span class="service-icon" role="img" aria-label="Box packing icon"></span>Box Packing</div>
  <div class="abs service" style="left:233px"><span class="service-icon" role="img" aria-label="Wrapping icon"></span>Wrapping</div>
  <div class="abs service" style="left:307px"><span class="service-icon" role="img" aria-label="Dismantling tools icon"></span>Dismantling</div>
  <div class="abs service" style="left:382px"><span class="service-icon" role="img" aria-label="Delivery truck icon"></span>Box Delivery</div>
  <p class="abs perks">We provide free insurance &nbsp;•&nbsp; Dedicated Cape Town experts</p>

  <footer class="abs footer" style="top:539px">
    <div class="abs f-contact" style="left:93px;top:12px">
      <div>✉&nbsp; bookings@blueridgehaulers.co.za</div>
      <div>☎&nbsp; 021 555 0142</div>
      <span class="f-btn">Instant Quote</span>
    </div>
    <div class="abs f-social" style="left:242px;top:21px"><span></span><span></span><span></span><span></span></div>
    <div class="abs f-links" style="left:376px;top:12px"><div>Terms and Conditions</div><div>FAQ</div><div>Blog</div><div>Contact</div></div>
    <div class="abs f-rule" style="left:80px;top:60px;width:368px"></div>
    <div class="abs f-copy" style="top:67px">Copyright © 2018 Blue Ridge Haulers. All rights reserved.</div>
  </footer>
</section>

<!-- QUOTE PAGE -->
<section class="page quote">
  <header class="abs q-header">
    <div class="abs brand" style="left:80px;top:15px"><span class="brand-mark"></span>BLUE RIDGE HAULERS</div>
    <nav class="abs nav" style="left:205px">
      <span style="width:42px">SERVICES</span>
      <span style="width:63px">WHY CHOOSE US</span>
      <span style="width:40px">ARTICLES</span>
      <span>CONTACT US</span>
    </nav>
    <div class="abs btn-logout" style="left:401px;top:15px;background:var(--tab-active)">LOGOUT</div>
  </header>
  <div class="abs tabs">
    <div class="tab" style="width:182px">LOCATIONS</div>
    <div class="tab" style="width:83px">ITEMS</div>
    <div class="tab" style="width:90px">EXTRAS</div>
    <div class="tab active" style="width:84px">PRICE</div>
  </div>

  <div class="abs vehicle-sec"></div>
  <h2 class="abs q-heading" style="left:78px;top:89px;font-weight:400">Select your vehicle:</h2>
  <div class="abs vehicle" style="left:123px;width:136px">
    <div class="vehicle-art" role="img" aria-label="Illustration of a closed box truck"></div>
    <div class="vehicle-label"><span class="check"><svg width="7" height="6" viewBox="0 0 7 6"><path d="M.6 3 2.6 5 6.4 .8" fill="none" stroke="#0b1d93" stroke-width="1.3"/></svg></span>Closed Truck</div>
  </div>
  <div class="abs vehicle" style="left:273px;width:135px">
    <div class="vehicle-art" role="img" aria-label="Illustration of a flat bed truck"></div>
    <div class="vehicle-label"><span class="check"></span>Flat Bed</div>
    <div class="vehicle-note">We use a canvas cover to keep your items dry if it rains</div>
  </div>

  <div class="abs date-sec" role="img" aria-label="Faded street scene of Cape Town with a removal truck and parked cars"></div>
  <h2 class="abs date-heading" style="font-weight:400">Select your date:</h2>
  <div class="abs cal">
    <div class="cal-head">
      <svg width="6" height="9" viewBox="0 0 6 9"><path d="M5 .8 1.2 4.5 5 8.2" fill="none" stroke="#fff" stroke-width="1.4"/></svg>
      <span>APRIL 22, 2012</span>
      <svg width="6" height="9" viewBox="0 0 6 9"><path d="M1 .8 4.8 4.5 1 8.2" fill="none" stroke="#fff" stroke-width="1.4"/></svg>
    </div>
    <div class="cal-grid">
      <div class="dow">SU</div><div class="dow">MO</div><div class="dow">TU</div><div class="dow">WE</div><div class="dow">TH</div><div class="dow">FR</div><div class="dow">SA</div>
    </div>
    <div class="cal-grid">
      <div class="day">1</div><div class="day">2</div><div class="day">3</div><div class="day">4</div><div class="day">5</div><div class="day">6</div><div class="day">7</div>
      <div class="day">8</div><div class="day">9</div><div class="day">10</div><div class="day">11</div><div class="day">12</div><div class="day">13</div><div class="day">14</div>
      <div class="day">15</div><div class="day">16</div><div class="day">17</div><div class="day">18</div><div class="day">19</div><div class="day">20</div><div class="day">21</div>
      <div class="day sel">22<small>R5840</small></div><div class="day">23<small>R5840</small></div><div class="day">24<small>R5840</small></div><div class="day">25<small>R7840</small></div><div class="day">26<small>R7840</small></div><div class="day">27<small>R7840</small></div><div class="day">28<small>R7840</small></div>
      <div class="day">29<small>R7840</small></div><div class="day">30<small>R7840</small></div><div class="day"></div><div class="day"></div><div class="day"></div><div class="day"></div><div class="day"></div>
    </div>
  </div>

  <h2 class="abs price-heading" style="font-weight:400">Price:</h2>
  <div class="abs price-box">
    <div class="row" style="top:15px">The move:<span class="val">R3000</span></div>
    <div class="row" style="top:35px">Wrapping:<span class="val">R700</span></div>
    <div class="row" style="top:56px">Hoisting:<span class="val">R1200</span></div>
    <div class="row" style="top:76px">Box Packing:<span class="val">R780</span></div>
    <div class="row" style="top:96px">Items not in lift<span class="val">R160</span></div>
    <div class="row total" style="top:118px">Total:<span class="val">R5840</span><span class="note">All inclusive</span></div>
    <div class="row plain" style="top:137px">Accept Terms and Conditions<span class="tick-box"></span></div>
    <div class="row plain" style="top:158px">Read reviews on SearchPro, FriendWall and RateLocal</div>
    <div class="row plain" style="top:179px">Goods in transit insurance up to R100 000 included free</div>
  </div>
  <div class="abs radio" style="top:848px"><i><b></b></i>Please contact me to arrange a time for my move</div>
  <div class="abs radio" style="top:864px"><i></i>Please just email me the quote for now (I might want to book later</div>
  <div class="abs btn" style="left:355px;top:886px;width:58px;height:17px;background:var(--blue)">Submit</div>
  <div class="abs btn" style="left:338px;top:909px;width:45px;height:14px;background:var(--grey-btn)">Back</div>
  <div class="abs btn" style="left:386px;top:909px;width:45px;height:14px;background:var(--green)">Save move</div>

  <footer class="abs footer" style="top:930px">
    <div class="abs f-contact" style="left:97px;top:12px">
      <div>✉&nbsp; bookings@blueridgehaulers.co.za</div>
      <div>☎&nbsp; 021 555 0142</div>
      <span class="f-btn">Instant Quote</span>
    </div>
    <div class="abs f-social" style="left:246px;top:21px"><span></span><span></span><span></span><span></span></div>
    <div class="abs f-links" style="left:382px;top:12px"><div>Terms and Conditions</div><div>FAQ</div><div>Blog</div><div>Contact</div></div>
    <div class="abs f-rule" style="left:70px;top:60px;width:380px"></div>
    <div class="abs f-copy" style="top:67px">Copyright © 2018 Blue Ridge Haulers. All rights reserved.</div>
  </footer>
</section>

</body>
</html>
```